依頼概要
■依頼の目的
マタニティさん向けの本の表紙デザインをお願いします。

■本の内容
胎内記憶による、しあわせな出産と育児のためのマタニティライフの過ごし方

第一章 胎内記憶を知ってマタニティライフを過ごしましょう
第二章 おなかの赤ちゃんとコミュニケーション
第三章 しあわせなお産をしよう
第四章 出産後のことを考えておこう
第五章 0歳育児が大切なことは意外と知られていない
第六章 夫婦で妊娠出産を楽しむ~産後うつを防ぐ~

差し支えなければですが、「0歳児についてわかるサブキャッチ」を表紙にデザインしたいのでよろしくお願いします。

■デザイン要望
柔らかい雰囲気の若いママ向けのおしゃれな感じが望ましいです。

■著者の記載

全国育み言葉研究会認定講師
マタニティライフしあわせアドバイザー
北浦ミレーユ詩織

※どこかに
「胎内記憶の世界的第一人者
森下晃先生 推薦」を入れてほしいです。

その他 ご不明な点がございましたらお気軽にご質問下さい。
よろしくお願いいたします。
書き損じておりました。
電子書籍(Pagora)での出版になります。

画像サイズは
表紙ファイルの理想的な寸法は2560×1600ピクセルです。
画像の寸法は1000×625ピクセル以上であることが必要です。

次点、次次点のかたへの参加報酬を設定いたしました。
皆様の自由な発想のデザインを楽しみにしております。

その他、必要な情報がありましたらお問い合わせください。
ランサーのみなさま、たくさんおご提案ありがとうございました。
どれも秀逸で感動しております。
2月末までに決定させていただきたいと思います。
よろしくお願いいたします。
■ 選んだ理由

どれもかわいいデザインで迷いましたが、
美しい写真でクオリティが高いこと、一目でマタニティの本であるとわかること、
「お産が楽になる」という言葉を大きく書いてくださっているのを選ぶようにとアドバイスされました。

■ 提案者全員のお礼・コメント

自分ではとうてい思いつかないような、かわいくてわかりやすいデザインを考えてくださり、感動しました。原稿を読んで下さり、内容も考慮して下さって感謝の気持ちで一杯です。
本当に迷いました。今回はご縁がなかったかたも、すばらしいものばかりでした。ありがとうございました!!

```html
<!DOCTYPE html>
<html lang="ja">
<head>
<meta charset="utf-8">
<title>ママが楽になる 胎児の記憶のひみつ</title>
<link rel="stylesheet" href="https://fonts.googleapis.com/css2?family=Zen+Maru+Gothic:wght@500;700;900&display=swap">
<style>
  :root {
    --coral-deep: #ec7b78;
    --coral-mid: #f29690;
    --coral-light: #f7b6ad;
    --ink: #5a1d26;
    --ink-soft: #6b2a30;
    --white: #ffffff;
    --badge-yellow: #f8e76a;
    --badge-red: #d9324a;
  }
  * { margin: 0; padding: 0; box-sizing: border-box; }
  html, body { width: 751px; height: 1200px; overflow: hidden; }
  body { font-family: "Zen Maru Gothic", sans-serif; color: var(--ink); }

  .cover {
    position: relative;
    width: 751px; height: 1200px;
    overflow: hidden;
    background:
      radial-gradient(circle at 30% 20%, rgba(255,255,255,0.18), transparent 45%),
      radial-gradient(circle at 80% 75%, rgba(255,220,210,0.25), transparent 50%),
      linear-gradient(180deg, var(--coral-light) 0%, var(--coral-mid) 35%, var(--coral-deep) 70%, var(--coral-mid) 100%);
  }

  .kicker {
    position: absolute; top: 55px; left: 150px; width: 440px; height: 100px;
    border-top: 2px solid var(--ink-soft);
    border-bottom: 2px solid var(--ink-soft);
    text-align: center;
  }
  .kicker-text {
    display: inline-block; padding-top: 22px;
    font-size: 44px; font-weight: 700; letter-spacing: 2px; color: var(--ink);
  }
  .kicker-text rt { font-size: 18px; font-weight: 500; }
  .kicker-text .accent { font-size: 56px; }

  .title-panel {
    position: absolute; top: 168px; left: 50px; width: 650px; height: 150px;
    background: var(--white); border-radius: 40px;
    box-shadow: 0 4px 18px rgba(150, 50, 50, 0.12);
  }
  .title-main {
    position: absolute; top: 12px; left: 0; width: 100%;
    text-align: center;
    font-size: 112px; font-weight: 900; letter-spacing: 4px; color: var(--ink);
    line-height: 1.1;
  }
  .title-sub {
    position: absolute; top: 292px; right: 40px;
    font-size: 66px; font-weight: 900; color: var(--ink); line-height: 1.1;
  }

  .lead {
    position: absolute; top: 382px; left: 80px;
    color: var(--ink); font-weight: 700; line-height: 1.35;
  }
  .lead-line1 { font-size: 34px; letter-spacing: 2px; }
  .lead-line2 { font-size: 29px; letter-spacing: 1px; }

  .illustration {
    position: absolute; top: 470px; left: 60px; width: 630px; height: 330px;
    border-radius: 50%;
    background: radial-gradient(ellipse at center, rgba(255,214,196,0.85) 0%, rgba(250,190,172,0.55) 50%, rgba(240,150,140,0) 75%);
  }

  .bubble {
    position: absolute; width: 185px; height: 185px; border-radius: 50%;
    background: var(--white);
    display: flex; flex-direction: column; align-items: center; justify-content: center;
    text-align: center; color: var(--ink);
  }
  .bubble-infant { left: 330px; top: 795px; }
  .bubble-birth { left: 515px; top: 775px; }
  .bubble-small { font-size: 17px; font-weight: 500; }
  .bubble-large { font-size: 38px; font-weight: 900; line-height: 1.15; margin: 6px 0 4px; }
  .bubble-birth .bubble-large { font-size: 42px; margin: 0 0 6px; }

  .endorsement {
    position: absolute; left: 12px; top: 925px; width: 190px; height: 180px;
    background: var(--badge-yellow); border-radius: 22px;
    text-align: center; color: var(--ink);
  }
  .endorsement-label {
    display: block; width: 164px; margin: 10px auto 0;
    background: var(--badge-red); color: var(--white);
    border-radius: 14px; font-size: 36px; font-weight: 900; letter-spacing: 6px; line-height: 50px;
  }
  .endorsement-role { font-size: 18px; font-weight: 700; line-height: 1.3; margin-top: 8px; }
  .endorsement-name { font-size: 36px; font-weight: 900; margin-top: 2px; }
  .endorsement-name small { font-size: 20px; font-weight: 700; }

  .author {
    position: absolute; left: 275px; top: 985px;
    color: var(--ink);
  }
  .author-org, .author-title { font-size: 26px; font-weight: 700; line-height: 1.45; }
  .author-name { font-size: 46px; font-weight: 900; letter-spacing: 2px; margin-top: 8px; }
</style>
</head>
<body>
  <main class="cover">
    <header class="kicker">
      <span class="kicker-text">ママが<ruby class="accent">楽<rt>ラク</rt></ruby>になる</span>
    </header>

    <section class="title-panel">
      <h1 class="title-main">胎児の記憶</h1>
    </section>
    <div class="title-sub">のひみつ</div>

    <p class="lead">
      <span class="lead-line1">ふたりで知る</span><br>
      <span class="lead-line2">おなかの赤ちゃんとの心のつながり</span>
    </p>

    <div class="illustration" role="img" aria-label="ふわふわと浮かぶ赤ちゃんたちのイラスト"></div>

    <div class="bubble bubble-infant">
      <span class="bubble-small">人生の土台となる</span>
      <span class="bubble-large">0歳育児</span>
      <span class="bubble-small">がよく分かる</span>
    </div>
    <div class="bubble bubble-birth">
      <span class="bubble-large">笑顔の<br>お産</span>
      <span class="bubble-small">をしよう</span>
    </div>

    <aside class="endorsement">
      <span class="endorsement-label">推薦</span>
      <p class="endorsement-role">胎内記憶の<br>世界的第一人者</p>
      <p class="endorsement-name">森下晃<small>先生</small></p>
    </aside>

    <footer class="author">
      <p class="author-org">全国育み言葉研究会認定講師</p>
      <p class="author-title">マタニティライフしあわせアドバイザー</p>
      <p class="author-name">北浦ミレーユ詩織</p>
    </footer>
  </main>
</body>
</html>
```